Brochure Design Crest Harbour Advisory

Create a brochure, which sells my business. Utilise the website www.crestharbouradvisory.example for the details that need to go into the brochure. I would like 2 designs, one for a 4 page brochure and the other for a two page brochure (focus firstly on the 4 page).

The focus points are our 4 year rent guarantee and also out pitch that we are invested with them. Please see the website.

Need to focus on the main points as per the website, can use text from the website and the graphics where suitable.

On the 4 page brochure, first 3 pages to be info as per the website. On the 4 page of the brochure I would like the information included on the final 2 pages of the attached document (the investment property example). Please shrink this down, you do not need to include all the wording more so the figures.

The colours of the brochure to be blue, white and black

Target Market(s)

Property Investors

Industry/Entity Type

Business

Colors
0355a3
ffffff

Requirements
Must have
• Must have the main info on the website, (4 year rent guarantee) 'We are invested with you'
Nice to have
• Professional look

```html
<!DOCTYPE html>
<html lang="en">
<head>
<meta charset="utf-8">
<title>Crest Harbour Advisory – Brochure</title>
<link rel="stylesheet" href="https://fonts.googleapis.com/css2?family=Michroma&family=Oswald:wght@500;700&family=Open+Sans:wght@400;600;700&family=Tinos:wght@400;700&display=swap">
<style>
:root{
  --cyan:#1ba1dd;
  --cyan-dark:#0f86c0;
  --navy:#0355a3;
  --black:#0a0a0a;
  --white:#ffffff;
  --ink:#222;
  --grey:#8a8a8a;
  --red:#e0141b;
  --stage:#d9dadc;
  --wide:"Michroma",sans-serif;
  --cond:"Oswald",sans-serif;
  --body:"Open Sans",sans-serif;
  --serif:"Tinos",serif;
}
*{box-sizing:border-box;margin:0;padding:0}
html,body{width:900px;height:1200px;overflow:hidden}
body{background:var(--stage);font-family:var(--body);color:var(--ink);position:relative}
.page{position:absolute;width:340px;height:476px;background:var(--white);overflow:hidden;box-shadow:0 6px 14px rgba(0,0,0,.18)}
.page > *{position:absolute}
.bg{left:0;top:0;width:340px;height:476px}

/* brand lockup */
.brand{display:flex;align-items:center;gap:6px}
.brand-mark{width:9px;height:9px;background:var(--cyan)}
.brand-name{font-family:var(--wide);color:var(--black);white-space:nowrap}

/* page 1 */
.cover{left:70px;top:124px}
.cover .brand{left:92px;top:28px}
.cover .brand-name{font-size:9.5px}
.hero-photo{left:0;top:69px;width:340px;height:131px;background:linear-gradient(180deg,#3a3a3a 0%,#8d8d8d 55%,#e6e6e6 100%)}
.tagline{top:211px;left:10px;font-family:var(--wide);font-size:14.5px;color:var(--white);letter-spacing:.2px;white-space:nowrap}
.about-title{left:18px;top:250px;font-family:var(--wide);font-size:11px;white-space:nowrap}
.about-title .box{background:var(--white);color:var(--black);padding:0 3px}
.about-title .accent{color:var(--cyan)}
.about-text{left:18px;top:268px;width:185px;font-size:5.2px;line-height:1.45;color:var(--white)}
.about-text p+p{margin-top:3px}
.lock-art{left:230px;top:262px;width:90px;height:118px;border-radius:45px 45px 40px 40px;background:radial-gradient(circle at 50% 65%,#2f7fc1 0%,#9fb8cc 45%,#e9edf0 75%)}
.portrait{left:16px;top:343px;width:42px;height:52px;background:linear-gradient(180deg,#dfe3e6,#a9b1b8);border:1px solid #fff}
.agent-name{left:64px;top:354px;font-family:var(--cond);font-weight:500;font-size:8px;color:var(--cyan)}
.agent-phone{left:64px;top:366px;font-family:var(--cond);font-weight:500;font-size:8px;color:var(--white);display:flex;align-items:center;gap:2px}
.agent-role{left:16px;top:403px;font-size:4.2px;color:var(--cyan);text-decoration:underline;font-weight:700}
.agent-mail{left:16px;top:410px;font-size:4px;color:var(--white)}
.badge{width:62px;height:62px}
.cover .badge{left:147px;top:385px}
.badge-text{font-family:var(--cond);font-weight:700;text-align:center;line-height:.95;color:var(--black)}
.cover .badge-text{left:147px;top:393px;width:62px}
.badge-text .num{display:block;font-size:17px;color:var(--cyan)}
.badge-text .yr{display:block;font-size:11px}
.cover .guarantee{left:215px;top:400px;font-family:var(--cond);font-weight:500;font-size:17px;color:var(--black);letter-spacing:.3px}
.guarantee .accent{color:var(--cyan)}
.foot-addr{left:12px;top:460px;font-size:4.4px;font-family:var(--cond);color:var(--white);display:flex;align-items:center;gap:2px;white-space:nowrap}
.foot-web{left:216px;top:460px;font-size:4.4px;font-family:var(--cond);color:var(--white);white-space:nowrap;display:flex;align-items:center;gap:2px}

/* page 2 */
.difference{left:490px;top:124px}
.difference-title{left:26px;top:22px;font-family:var(--wide);font-size:19px;white-space:nowrap;color:var(--white)}
.difference-title .dark{color:var(--black)}
.difference .badge{left:22px;top:66px;width:74px;height:74px}
.difference .badge-text{left:22px;top:76px;width:74px}
.difference .badge-text .num{font-size:21px}
.difference .badge-text .yr{font-size:14px}
.difference .guarantee{left:120px;top:84px;font-family:var(--cond);font-weight:700;font-size:21px;color:var(--black)}
.risk{left:80px;top:136px;font-family:var(--cond);font-weight:700;font-size:16px;color:var(--black)}
.risk .accent{color:var(--navy)}
.features{left:0;top:166px;width:340px;height:62px;display:flex;justify-content:space-around;padding:10px 24px 0}
.feature{display:flex;flex-direction:column;align-items:center;gap:4px;width:70px}
.feature-icon{width:28px;height:28px;border:1.5px solid var(--white);border-radius:50%;display:flex;align-items:center;justify-content:center}
.feature-label{font-family:var(--cond);font-weight:500;font-size:5.6px;color:var(--white);text-decoration:underline;white-space:nowrap}
.section-title{left:0;width:340px;top:240px;text-align:center;font-family:var(--wide);font-size:13px;color:var(--black);white-space:nowrap}
.section-title .accent{color:var(--cyan)}
.section-title span.under{border-bottom:2px solid var(--black);padding-bottom:1px}
.property{top:270px;width:96px;height:134px;border:1.5px solid var(--cyan);border-radius:7px;padding:24px 7px 0;text-align:center}
.property-icon{position:absolute;left:35px;top:-12px;width:26px;height:26px;border-radius:50%;background:var(--cyan);border:2px solid var(--white);display:flex;align-items:center;justify-content:center;color:var(--white);font-family:var(--body);font-weight:700;font-size:13px}
.property h3{font-family:var(--cond);font-weight:500;font-size:5.8px;line-height:1.3;color:var(--cyan);text-transform:uppercase;min-height:16px}
.property p{margin-top:4px;font-size:4.3px;line-height:1.42;text-align:justify;color:var(--ink)}
.prop-a{left:13px}.prop-b{left:122px}.prop-c{left:231px}
.contact{left:26px;top:422px;color:var(--white);font-family:var(--cond)}
.contact .name{font-size:7.6px;font-weight:500;color:var(--cyan)}
.contact .name b{color:var(--white);margin-left:6px;font-weight:500}
.contact .line{font-size:4.2px;margin-top:2px;font-family:var(--body)}
.difference .brand{left:222px;top:440px}
.difference .brand-name{font-size:6.8px}

/* page 3 */
.example{left:294px;top:650px}
.example-title{left:22px;top:17px;font-family:var(--wide);font-size:6.2px;color:var(--black);white-space:nowrap}
.example-title .accent{color:var(--cyan)}
.example .brand{left:205px;top:22px}
.example .brand-name{font-size:6.4px}
.tablet-art{left:24px;top:40px;width:135px;height:80px;transform:rotate(-8deg);border-radius:6px;background:linear-gradient(160deg,#eef1f3 0%,#7f93a6 50%,#2e3b47 100%);border:3px solid #f5f5f5;box-shadow:0 3px 6px rgba(0,0,0,.3)}
.data-table{border:1.2px solid #333;border-radius:5px;overflow:hidden;font-size:5px;background:var(--white)}
.data-table table{width:100%;border-collapse:collapse}
.data-table th{background:var(--cyan);color:var(--black);font-family:var(--serif);font-size:7px;font-weight:700;text-align:left;padding:2px 4px}
.data-table th.num{text-align:center}
.data-table td{padding:1.6px 4px;border-bottom:.6px solid #cfcfcf;font-family:var(--body)}
.data-table td.num{text-align:right}
.data-table tr.hl td{background:var(--cyan);color:var(--white);font-weight:700}
.red{color:var(--red)}
.costs{left:174px;top:48px;width:145px}
.band{left:0;width:340px;height:9px;background:var(--cyan);color:var(--white);text-align:center;font-family:var(--wide);font-size:6.6px;line-height:9px}
.band-a{top:128px}.band-b{top:254px}
.intro{left:16px;width:310px;font-size:4.8px;line-height:1.35;color:var(--ink)}
.intro-a{top:140px}
.intro-b{top:266px;text-align:center}
.holding{left:18px;top:173px;width:98px}
.profit{left:120px;top:173px;width:98px}
.tax{left:222px;top:173px;width:102px}
.growth-label{left:0;width:340px;top:283px;text-align:center;font-family:var(--serif);font-size:6.5px;font-weight:700;color:var(--red)}
.growth-label span{border-bottom:.8px solid var(--red)}
.chart{left:60px;top:296px;width:240px;height:116px}
.projection{left:24px;top:406px;width:300px}
.projection th{text-align:center}
.projection td{text-align:center}
.projection td:first-child{text-align:left;font-weight:600}
.example-foot{left:0;top:453px;width:340px;height:23px}
.example-web{left:0;top:459px;width:340px;text-align:center;font-family:var(--body);font-size:9px;letter-spacing:4px;color:var(--white)}
</style>
</head>
<body>

<!-- Page 1: cover -->
<section class="page cover" aria-label="Brochure cover">
  <svg class="bg" viewBox="0 0 340 476" aria-hidden="true">
    <rect x="276" y="0" width="29" height="28" fill="#0a0a0a"/>
    <rect x="305" y="28" width="35" height="35" fill="#1ba1dd"/>
    <rect x="0" y="64" width="305" height="5" fill="#1ba1dd"/>
    <rect x="0" y="200" width="340" height="3" fill="#1ba1dd"/>
    <polygon points="0,204 210,204 206,240 0,240" fill="#0a0a0a"/>
    <polygon points="210,204 340,204 340,240 206,240" fill="#1ba1dd"/>
    <polygon points="0,244 226,244 117,452 0,452" fill="#0a0a0a"/>
    <polygon points="232,244 240,244 131,452 123,452" fill="#1ba1dd"/>
    <rect x="210" y="392" width="130" height="1.5" fill="#1ba1dd"/>
    <rect x="210" y="424" width="130" height="1.5" fill="#1ba1dd"/>
    <polygon points="178,383 210,415 178,447 146,415" fill="#fff" stroke="#1ba1dd" stroke-width="3"/>
    <polygon points="0,452 202,452 190,476 0,476" fill="#1ba1dd"/>
    <polygon points="202,452 340,452 340,476 190,476" fill="#0a0a0a"/>
  </svg>
  <div class="brand"><span class="brand-mark"></span><span class="brand-name">Crest Harbour Advisory</span></div>
  <div class="hero-photo" role="img" aria-label="Photo of a businessman in a suit touching a city skyline"></div>
  <h1 class="tagline">WE ARE INVESTED&nbsp;&nbsp;WITH YOU</h1>
  <h2 class="about-title"><span class="box">ABOUT</span> <span class="accent">CHA</span></h2>
  <div class="about-text">
    <p>Crest Harbour Advisory is a property consulting firm which assists clients grow strong investment property portfolios.</p>
    <p>Unlike other groups we put our money where our mouth is and provide a 4-year rental guarantee on our properties. This allows us to share your risk and gives CHA clients trust and reassurance that we are working for them, not for a commission fee.</p>
  </div>
  <div class="lock-art" role="img" aria-label="Illustration of a blue combination padlock"></div>
  <div class="portrait" role="img" aria-label="Portrait photo of the property consultant"></div>
  <div class="agent-name">Daniel Marsh</div>
  <div class="agent-phone">
    <svg width="6" height="6" viewBox="0 0 10 10" aria-hidden="true"><path d="M2 1l2 2-1 1.5c.8 1.4 1.6 2.2 3 3L7.5 6l2 2-1.5 1.5C4.5 9 1 5.5.5 2.5z" fill="#fff"/></svg>
    0400 555 018
  </div>
  <div class="agent-role">Property Consultant</div>
  <div class="agent-mail">daniel@crestharbouradvisory.example</div>
  <div class="badge-text"><span class="num">4</span><span class="yr">YEAR</span></div>
  <div class="guarantee">RENT <span class="accent">GUARANTEE</span></div>
  <div class="foot-addr">
    <svg width="5" height="6" viewBox="0 0 10 12" aria-hidden="true"><path d="M5 0a4 4 0 0 1 4 4c0 3-4 8-4 8S1 7 1 4a4 4 0 0 1 4-4z" fill="#fff"/></svg>
    Level 3, Harbour Point, 12 Wattle Court, Eastwood 2122
  </div>
  <div class="foot-web">
    <svg width="6" height="6" viewBox="0 0 10 10" aria-hidden="true"><circle cx="5" cy="5" r="4" fill="none" stroke="#fff" stroke-width="1.2"/></svg>
    www.crestharbouradvisory.example
  </div>
</section>

<!-- Page 2: the difference -->
<section class="page difference" aria-label="The CHA difference">
  <svg class="bg" viewBox="0 0 340 476" aria-hidden="true">
    <polygon points="0,0 132,0 170,78 0,78" fill="#1ba1dd"/>
    <polygon points="0,78 60,78 60,160 0,160" fill="#1ba1dd"/>
    <rect x="60" y="78" width="280" height="2" fill="#0a0a0a"/>
    <rect x="96" y="80" width="244" height="36" fill="#1ba1dd"/>
    <rect x="60" y="116" width="280" height="2" fill="#1ba1dd"/>
    <rect x="60" y="158" width="280" height="2" fill="#1ba1dd"/>
    <polygon points="59,66 96,103 59,140 22,103" fill="#fff" stroke="#1ba1dd" stroke-width="3"/>
    <rect x="0" y="166" width="340" height="62" fill="#1ba1dd"/>
    <rect x="0" y="410" width="340" height="3" fill="#1ba1dd"/>
    <polygon points="0,413 190,413 220,476 0,476" fill="#1ba1dd"/>
    <polygon points="0,413 185,413 205,460 0,460" fill="#0a0a0a"/>
  </svg>
  <h1 class="difference-title">THE CHA <span class="dark">DIFFERENCE</span></h1>
  <div class="badge-text"><span class="num">4</span><span class="yr">YEAR</span></div>
  <div class="guarantee">RENT <span style="color:#fff">GUARANTEE</span></div>
  <h2 class="risk"><span class="accent">WE HELP</span> MINIMISE YOUR RISK</h2>
  <div class="features">
    <div class="feature">
      <div class="feature-icon"><svg width="14" height="14" viewBox="0 0 14 14" aria-hidden="true"><path d="M7 1a4 4 0 0 1 4 4c0 3-4 8-4 8S3 8 3 5a4 4 0 0 1 4-4z" fill="none" stroke="#fff" stroke-width="1.2"/><circle cx="7" cy="5" r="1.4" fill="#fff"/></svg></div>
      <span class="feature-label">LOW RISK LOCATIONS</span>
    </div>
    <div class="feature">
      <div class="feature-icon"><svg width="14" height="14" viewBox="0 0 14 14" aria-hidden="true"><rect x="2" y="2" width="10" height="10" fill="none" stroke="#fff" stroke-width="1.2"/><path d="M4.5 10V7M7 10V5M9.5 10V6" stroke="#fff" stroke-width="1.2"/></svg></div>
      <span class="feature-label">SOURCED DIRECT</span>
    </div>
    <div class="feature">
      <div class="feature-icon"><svg width="14" height="14" viewBox="0 0 14 14" aria-hidden="true"><circle cx="7" cy="7" r="5" fill="none" stroke="#fff" stroke-width="1.2"/><path d="M9.5 4.5L8 8 4.5 9.5 6 6z" fill="#fff"/></svg></div>
      <span class="feature-label">REAL INVESTORS</span>
    </div>
    <div class="feature">
      <div class="feature-icon"><svg width="14" height="14" viewBox="0 0 14 14" aria-hidden="true"><circle cx="9" cy="5" r="3" fill="none" stroke="#fff" stroke-width="1.2"/><path d="M7 7l-5 5M3.5 10.5l1.5 1.5" stroke="#fff" stroke-width="1.2"/></svg></div>
      <span class="feature-label">FULL TURN KEY</span>
    </div>
  </div>
  <h2 class="section-title"><span class="under"><span class="accent">OUR</span> PROPERTIES</span></h2>
  <article class="property prop-a">
    <div class="property-icon"><svg width="12" height="12" viewBox="0 0 12 12" aria-hidden="true"><path d="M2 10V8M5 10V6M8 10V4M1 6l4-3 2 1 4-3" stroke="#fff" stroke-width="1.4" fill="none"/></svg></div>
    <h3>High Growth<br>Properties</h3>
    <p>Our team selects homes in areas with strong population growth, new jobs and planned infrastructure, so the value of your asset can build steadily over time while the rent guarantee protects your yearly cash flow.</p>
  </article>
  <article class="property prop-b">
    <div class="property-icon"><svg width="13" height="12" viewBox="0 0 13 12" aria-hidden="true"><path d="M1 6.5L6.5 1 12 6.5M3 5v6h7V5" stroke="#fff" stroke-width="1.4" fill="none"/><rect x="5.3" y="7.5" width="2.4" height="3.5" fill="#fff"/></svg></div>
    <h3>Positively Geared<br>Properties Dual Dwellings</h3>
    <p>Dual dwelling homes earn two rents from a single block of land. The extra income helps cover holding costs from day one, making it easier to keep building a balanced and positively geared portfolio.</p>
  </article>
  <article class="property prop-c">
    <div class="property-icon">$</div>
    <h3>Self-Managed<br>Super Fund Solutions</h3>
    <p>We work with your accountant and adviser to source properties that suit a self-managed super fund, helping you use your retirement savings to hold quality residential property for the long term.</p>
  </article>
  <div class="contact">
    <div class="name">Daniel Marsh <b>&#9742; 0400 555 018</b></div>
    <div class="line">Property Consultant</div>
    <div class="line">daniel@crestharbouradvisory.example</div>
    <div class="line">&#9679; Level 3, Harbour Point, 12 Wattle Court, Eastwood 2122</div>
    <div class="line">&#9679; www.crestharbouradvisory.example</div>
  </div>
  <div class="brand"><span class="brand-mark"></span><span class="brand-name">Crest Harbour Advisory</span></div>
</section>

<!-- Page 3: investment property example -->
<section class="page example" aria-label="Investment property example">
  <svg class="bg" viewBox="0 0 340 476" aria-hidden="true">
    <rect x="304" y="0" width="18" height="18" fill="#0a0a0a"/>
    <rect x="322" y="18" width="18" height="18" fill="#1ba1dd"/>
    <polygon points="0,453 340,453 340,476 0,476" fill="#1ba1dd"/>
    <polygon points="0,458 12,458 4,476 0,476" fill="#0a0a0a"/>
    <polygon points="330,458 340,458 340,476 336,476" fill="#0a0a0a"/>
  </svg>
  <h1 class="example-title">INVESTMENT PROPERTY <span class="accent">EXAMPLE</span></h1>
  <div class="brand"><span class="brand-mark"></span><span class="brand-name">Crest Harbour Advisory</span></div>
  <div class="tablet-art" role="img" aria-label="Tablet showing a photo of a modern four bedroom home"></div>
  <div class="data-table costs">
    <table>
      <tr><th>Initial Costs</th><th class="num">$</th><th></th></tr>
      <tr><td>Stamp Duty</td><td>Stamp Duty</td><td>(land value<br>$212,000)</td></tr>
      <tr><td>Solicitor</td><td>1,200</td><td></td></tr>
      <tr><td>TOTAL</td><td>7,494*</td><td></td></tr>
    </table>
  </div>
  <div class="band band-a">Ongoing Holding Profit/Loss</div>
  <p class="intro intro-a">The below example is based on an investment property that Crest Harbour Advisory had available through one of our partners in 2016, it is representative of similar properties currently available through Crest Harbour Advisory. Property Facts;</p>
  <div class="data-table holding">
    <table>
      <tr><th>Holding Costs</th><th class="num">$</th></tr>
      <tr><td>Interest 4.2%**</td><td class="num">17,976</td></tr>
      <tr><td>Insurance</td><td class="num">800</td></tr>
      <tr><td>Council Rates</td><td class="num">1,800</td></tr>
      <tr><td>Management Fees</td><td class="num">1,755</td></tr>
      <tr><td>Management Fees</td><td class="num red">22,331</td></tr>
    </table>
  </div>
  <div class="data-table profit">
    <table>
      <tr><th>Profit/Loss</th><th class="num">$</th></tr>
      <tr><td>Rent received $450pw</td><td class="num">23,400</td></tr>
      <tr><td>less Holding costs</td><td class="num">(22,331)</td></tr>
      <tr><td>Gross Gain</td><td class="num">1,069</td></tr>
    </table>
  </div>
  <div class="data-table tax">
    <table>
      <tr><th>Tax Deduction</th><th class="num">$</th></tr>
      <tr><td>Gain</td><td class="num">-(1,069)</td></tr>
      <tr><td>Dep'n Fix and</td><td class="num">3,567</td></tr>
      <tr><td>Capital Write down</td><td class="num">4,850</td></tr>
      <tr class="hl"><td>TOTAL DEDUCTIONS</td><td class="num red">7,348</td></tr>
      <tr><td>Claimable Tax</td><td class="num">2,718</td></tr>
      <tr><td>PROFIT</td><td class="num" style="color:var(--cyan)">$3,787</td></tr>
    </table>
  </div>
  <div class="band band-b">Growth Projection</div>
  <p class="intro intro-b">Below is an example of what a property purchased today in South East Queensland can be expected to make<br>over the next 20 years based on a 6% growth rate.</p>
  <div class="growth-label"><span>6% GROWTH PER ANNUM</span></div>
  <svg class="chart" viewBox="0 0 240 116" role="img" aria-label="Bar chart of debt and capital gain over 20 years">
    <g font-family="Open Sans, sans-serif" font-size="5" fill="#222">
      <text x="34" y="16" text-anchor="end">1,500,000 -</text>
      <text x="34" y="28.5" text-anchor="end">1,250,000 -</text>
      <text x="34" y="41" text-anchor="end">1,000,000 -</text>
      <text x="34" y="53.5" text-anchor="end">750,000 -</text>
      <text x="34" y="66" text-anchor="end">500,000 -</text>
      <text x="34" y="78.5" text-anchor="end">250,000 -</text>
      <text x="52" y="101" text-anchor="middle">Current</text>
      <text x="82" y="101" text-anchor="middle">5 years</text>
      <text x="112" y="101" text-anchor="middle">10 years</text>
      <text x="142" y="101" text-anchor="middle">15 years</text>
      <text x="172" y="101" text-anchor="middle">20 years</text>
      <rect x="197" y="5" width="4" height="4" fill="#e0141b"/><text x="203" y="9">Debt</text>
      <rect x="197" y="21" width="4" height="4" fill="#1ba1dd"/><text x="203" y="25">Capital</text><text x="203" y="30">Gain</text>
    </g>
    <g>
      <rect x="40" y="73" width="24" height="21" fill="#e0141b"/>
      <rect x="70" y="65.8" width="24" height="7.2" fill="#1ba1dd"/>
      <rect x="70" y="73" width="24" height="21" fill="#e0141b"/>
      <rect x="100" y="56" width="24" height="17" fill="#1ba1dd"/>
      <rect x="100" y="73" width="24" height="21" fill="#e0141b"/>
      <rect x="130" y="43" width="24" height="30" fill="#1ba1dd"/>
      <rect x="130" y="73" width="24" height="21" fill="#e0141b"/>
      <rect x="160" y="25.4" width="24" height="47.6" fill="#1ba1dd"/>
      <rect x="160" y="73" width="24" height="21" fill="#e0141b"/>
    </g>
  </svg>
  <div class="data-table projection">
    <table>
      <tr><th></th><th>Current</th><th>5 years</th><th>10 years</th><th>15 years</th><th>20 yearst</th></tr>
      <tr><td>Property Value</td><td>$428,000</td><td>$572,790</td><td>$766,482</td><td>$1,025,726</td><td>$1,372,653</td></tr>
      <tr><td>Capital Gain</td><td>0</td><td>$144,790</td><td>$338,790</td><td>$597,726</td><td>$944,653</td></tr>
    </table>
  </div>
  <div class="example-web">www.crestharbouradvisory.example</div>
</section>

</body>
</html>
```